Briefpapier und Visitenkarten
Zielgruppe
In erster Linie mir selbst.
Aufgabenstellung
Gestaltung von Visitenkarten und Briefpapier.
Visitenkarten: Gestaltung beidseitig und in Pantone Farben
Briefpapier: Gestaltung einseitig und in Pantone Farben
Briefpapier und Visitenkarten sollen ein Design haben.

```html
<!DOCTYPE html>
<html lang="de">
<head>
<meta charset="utf-8">
<title>Kolthaus Werbeagentur – Visitenkarten</title>
<link rel="stylesheet" href="https://fonts.googleapis.com/css2?family=Montserrat:wght@600&family=Arimo:wght@400&display=swap">
<style>
  :root {
    --page: #ffffff;
    --card: #ffffff;
    --card-edge: #d6d6d6;
    --brand-grey: #8c8c8c;
    --text-grey: #9a9a9a;
    --faint: #f0f0f0;
  }
  html, body {
    margin: 0;
    width: 1200px;
    height: 1200px;
    overflow: hidden;
    background: var(--page);
  }
  .card {
    position: absolute;
    left: 305px;
    width: 607px;
    height: 393px;
    background: var(--card);
    border: 1px solid var(--card-edge);
    box-sizing: border-box;
    overflow: hidden;
  }
  .card--front { top: 132px; }
  .card--back  { top: 675px; }

  .front__mark {
    position: absolute;
    left: 235px;
    top: 55px;
    width: 136px;
    height: 136px;
    border-radius: 50%;
    background: var(--brand-grey);
  }
  .front__name {
    position: absolute;
    left: 0;
    right: 0;
    top: 240px;
    margin: 0;
    text-align: center;
    font-family: "Montserrat", sans-serif;
    font-weight: 600;
    font-size: 31px;
    letter-spacing: 0.08em;
    color: var(--brand-grey);
  }
  .front__tagline {
    position: absolute;
    left: 0;
    right: 0;
    top: 284px;
    margin: 0;
    text-align: center;
    font-family: "Montserrat", sans-serif;
    font-weight: 600;
    font-size: 13px;
    letter-spacing: 0.5em;
    color: var(--brand-grey);
  }

  .back__decor {
    position: absolute;
    left: 490px;
    top: -30px;
    width: 230px;
    height: 230px;
    border-radius: 50%;
    background: var(--faint);
  }
  .back__name {
    position: absolute;
    left: 37px;
    top: 30px;
    margin: 0;
    font-family: "Montserrat", sans-serif;
    font-weight: 600;
    font-size: 25px;
    letter-spacing: 0.05em;
    color: var(--brand-grey);
  }
  .back__address, .back__contact {
    position: absolute;
    left: 37px;
    margin: 0;
    font-family: "Arimo", sans-serif;
    font-size: 25px;
    line-height: 40px;
    color: var(--text-grey);
    font-style: normal;
  }
  .back__address { top: 100px; }
  .back__contact { top: 288px; }
  .back__bar {
    position: absolute;
    left: 0;
    bottom: 0;
    width: 482px;
    height: 8px;
    background: var(--brand-grey);
    opacity: 0.55;
  }
</style>
</head>
<body>
  <section class="card card--front">
    <div class="front__mark" aria-hidden="true"></div>
    <h1 class="front__name">KOLTHAUS WERBEAGENTUR</h1>
    <p class="front__tagline">IDEEN MIT WIRKUNG</p>
  </section>

  <section class="card card--back">
    <div class="back__decor" aria-hidden="true"></div>
    <h2 class="back__name">KOLTHAUS WERBEAGENTUR</h2>
    <address class="back__address">
      Inh. Jonas Brettner<br>
      Lindenallee 14<br>
      D-53119 Bonn
    </address>
    <p class="back__contact">
      E-Mail: info@kolthauswa.de<br>
      Website: www.kolthauswa.de
    </p>
    <div class="back__bar" aria-hidden="true"></div>
  </section>
</body>
</html>
```